Business card - PK Talent Partners / The Darwell Group

We need a business card and logo design for my executive search (recruiting / headhunting) firm. We find people to fill open jobs at companies. We are a U.S. based company and do some global work also. So maybe something with a globe but definitely looking for other options also. Maybe something incorporating the letters PK which is our current logo but looking at options. The card should say BOTH full company names and tag line-

PK Talent Partners / The Darwell Group
Executive Search Results You Can Count On

The design should say about the company-
Sharp
Reliable
Find the best people for the job
Business oriented
Results achieved
Modern

Target Market(s)

Business owners, CEO's, and heads of human resources departments

Industry/Entity Type

Business Consultant

Contact Information for Business Card

The card MUST say BOTH full company names and tag line-

Logo Text

Logo does not NEED to say anything on the design itself, but could if designed that way.

Font styles to use
Serif
Sans Serif

Requirements
Must have
• The business cards need to have. In addition to name, title, address, phone, website, and email address,
• The card MUST say BOTH full company names and tag line-
• PK Talent Partners / The Darwell Group
• Executive Search Results You Can Count On
Nice to have
• The design should say about the company-
• Sharp
• Reliable
• Find the best people for the job
• Business oriented
• Results achieved
• Modern
• Maybe something with a globe or the letters PK or relating to people. Open to options.
Should not have
• Should not be cutesy or funny, for this design

```html
<!DOCTYPE html>
<html lang="en">
<head>
<meta charset="utf-8">
<title>PK Talent Partners – Business Card</title>
<link href="https://fonts.googleapis.com/css2?family=Marcellus+SC&family=Open+Sans:wght@400;600;700&display=swap" rel="stylesheet">
<style>
  :root {
    --page: #ecebe8;
    --dark-top: #3a3a3a;
    --dark-bottom: #161616;
    --light-top: #fbfbfb;
    --light-bottom: #d6d6d6;
    --green: #6ab023;
    --green-deep: #4f8c14;
    --silver: #cfcfcf;
    --ink: #333333;
    --ink-soft: #4a4a4a;
    --white: #ffffff;
  }
  * { box-sizing: border-box; margin: 0; padding: 0; }
  html, body { width: 1200px; height: 1024px; overflow: hidden; }
  body { background: var(--page); position: relative; font-family: "Open Sans", sans-serif; }

  .card {
    position: absolute; left: 180px; width: 840px; height: 480px;
    overflow: hidden; border-radius: 4px;
    box-shadow: 0 6px 18px rgba(0,0,0,.18);
  }
  .card--front { top: 24px; background: radial-gradient(ellipse at 45% 35%, var(--dark-top), var(--dark-bottom) 75%); }
  .card--back { top: 520px; background: linear-gradient(135deg, var(--light-top), var(--light-bottom)); }

  .wave { position: absolute; inset: 0; width: 100%; height: 100%; }

  /* brand block */
  .brand-name {
    display: flex; align-items: center; gap: 12px; white-space: nowrap;
    font-family: "Marcellus SC", serif; color: var(--silver); letter-spacing: 1px; line-height: 1.1;
  }
  .brand-mark { background: var(--silver); flex: none; }
  .brand-group {
    font-family: "Marcellus SC", serif; color: var(--silver); letter-spacing: 1px; white-space: nowrap;
  }

  /* front */
  .front-brand { position: absolute; left: 50px; top: 262px; }
  .front-brand .brand-name { font-size: 32px; }
  .front-brand .brand-mark { width: 18px; height: 18px; }
  .front-brand .brand-group { font-size: 18px; margin: 4px 0 0 30px; }
  .front-tagline {
    margin-top: 14px; font-weight: 700; font-size: 16px; color: var(--green); white-space: nowrap;
  }
  .divider {
    position: absolute; left: 392px; top: 50px; width: 1px; height: 180px;
    background: linear-gradient(to bottom, transparent, #6a6a6a 40%, transparent);
  }
  .person { position: absolute; left: 420px; top: 52px; }
  .person-name { font-family: "Marcellus SC", serif; font-size: 28px; color: var(--white); letter-spacing: 1px; }
  .person-title { font-family: "Marcellus SC", serif; font-size: 17px; color: var(--green); margin-top: 2px; letter-spacing: .5px; }
  .contacts { list-style: none; margin-top: 24px; }
  .contacts li {
    display: flex; align-items: center; gap: 12px;
    font-size: 14px; color: #e2e2e2; line-height: 26px;
  }
  .contacts svg { width: 14px; height: 14px; flex: none; }

  /* back */
  .back-brand { position: absolute; left: 300px; top: 140px; }
  .back-brand .brand-name { color: var(--ink); font-size: 46px; }
  .back-brand .brand-mark { background: var(--ink); width: 24px; height: 24px; }
  .back-brand .brand-group { color: var(--ink-soft); font-size: 24px; margin: 6px 0 0 38px; }
  .band {
    position: absolute; left: 0; right: 0; top: 300px; height: 46px;
    background: linear-gradient(to bottom, var(--green), var(--green-deep));
    display: flex; align-items: center; padding-left: 250px;
    color: var(--white); font-weight: 700; font-size: 20px;
  }
  .qualities { position: absolute; top: 362px; list-style: none; font-size: 16px; color: var(--ink-soft); line-height: 26px; font-weight: 600; }
  .qualities--plain { left: 30px; }
  .qualities--bulleted { left: 470px; }
  .qualities--bulleted li { display: flex; align-items: center; gap: 12px; }
  .qualities--bulleted li::before { content: ""; width: 7px; height: 7px; border-radius: 50%; background: var(--green); }
</style>
</head>
<body>

<section class="card card--front" aria-label="Business card front">
  <svg class="wave" viewBox="0 0 840 480" preserveAspectRatio="none" aria-hidden="true">
    <path d="M0,400 C300,425 540,400 660,320 C750,260 795,170 840,120 L840,480 L0,480 Z" fill="#e4e4e4"/>
    <path d="M0,425 C310,448 560,420 680,340 C765,285 805,200 840,160 L840,480 L0,480 Z" fill="var(--green)"/>
  </svg>

  <div class="front-brand">
    <div class="brand-name"><span class="brand-mark"></span>PK Talent Partners</div>
    <p class="brand-group">/ The Darwell Group</p>
    <p class="front-tagline">Executive Search Results You Can Count On</p>
  </div>

  <div class="divider"></div>

  <div class="person">
    <p class="person-name">Daniel Marsh</p>
    <p class="person-title">Managing Director</p>
    <ul class="contacts">
      <li><svg viewBox="0 0 14 14"><path d="M7 1a4 4 0 0 0-4 4c0 3 4 8 4 8s4-5 4-8a4 4 0 0 0-4-4zm0 5.5A1.5 1.5 0 1 1 7 3.5a1.5 1.5 0 0 1 0 3z" fill="var(--green)"/></svg>12 Harbour Lane, Westfield, WA 6000</li>
      <li><svg viewBox="0 0 14 14"><path d="M3 1l2.5 0 1 3-1.5 1.2a8 8 0 0 0 3.8 3.8L10 7.5l3 1V11a1.5 1.5 0 0 1-1.5 1.5A10.5 10.5 0 0 1 1.5 2.5 1.5 1.5 0 0 1 3 1z" fill="var(--green)"/></svg>0412 555 018</li>
      <li><svg viewBox="0 0 14 14"><rect x="1" y="3" width="12" height="8" rx="1" fill="var(--green)"/><path d="M1.5 3.5 7 8l5.5-4.5" stroke="#1e1e1e" stroke-width="1.2" fill="none"/></svg>daniel@pktalentpartners.com</li>
      <li><svg viewBox="0 0 14 14"><circle cx="7" cy="7" r="6" fill="var(--green)"/><path d="M1 7h12M7 1c-2.5 3-2.5 9 0 12M7 1c2.5 3 2.5 9 0 12" stroke="#1e1e1e" stroke-width="1" fill="none"/></svg>www.pktalentpartners.com</li>
    </ul>
  </div>
</section>

<section class="card card--back" aria-label="Business card back">
  <div class="back-brand">
    <div class="brand-name"><span class="brand-mark"></span>PK Talent Partners</div>
    <p class="brand-group">/ The Darwell Group</p>
  </div>
  <div class="band">Executive Search Results You Can Count On</div>
  <ul class="qualities qualities--plain">
    <li>Sharp</li>
    <li>Reliable</li>
    <li>Find the best people for the job</li>
  </ul>
  <ul class="qualities qualities--bulleted">
    <li>Business oriented</li>
    <li>Results achieved</li>
    <li>Modern</li>
  </ul>
</section>

</body>
</html>
```